Maple-hop Tots book cover

Enticing book cover
Book is for parents who want their children to be their best in life through wholesome natural means.
Includes topics on chiropractic care, movement, nutrition, supplementation, neurology, primitive reflexes, descriptions od children with ADHD, sensory processing disorders, Aspergers, etc.
Underneath is my logo, but that does not have to included

```html
<!DOCTYPE html>
<html lang="en">
<head>
<meta charset="utf-8">
<title>Maple-hop Tots — Book Cover</title>
<link href="https://fonts.googleapis.com/css2?family=Allura&family=Oswald:wght@300&family=Raleway:wght@300;400&display=swap" rel="stylesheet">
<style>
  :root {
    --cover-red: #ee3a2c;
    --title-red: #e8412f;
    --script-tan: #c39c7f;
    --cream-light: #fffbd9;
    --cream-mid: #f9efbc;
    --cream-edge: #f1dca0;
    --white: #ffffff;
  }
  html, body {
    margin: 0;
    padding: 0;
    width: 761px;
    height: 1200px;
    overflow: hidden;
    background: var(--white);
  }
  .cover {
    position: relative;
    width: 761px;
    height: 1200px;
    overflow: hidden;
    background: radial-gradient(ellipse 75% 60% at 50% 42%, var(--cream-light) 0%, var(--cream-mid) 55%, var(--cream-edge) 100%);
  }
  .top-band {
    position: absolute;
    left: 0; top: 0;
    width: 100%; height: 22px;
    background: var(--cover-red);
  }
  .top-rule {
    position: absolute;
    left: 0; top: 30px;
    width: 100%; height: 10px;
    background: var(--cover-red);
    box-shadow: 0 -8px 0 0 var(--white);
  }
  .series-title {
    position: absolute;
    left: 0; right: 0; top: 165px;
    margin: 0;
    text-align: center;
    font-family: "Raleway", sans-serif;
    font-weight: 300;
    font-size: 68px;
    letter-spacing: 1px;
    color: var(--title-red);
    line-height: 1;
  }
  .script-title {
    position: absolute;
    left: 0; right: 0; top: 250px;
    margin: 0;
    text-align: center;
    font-family: "Allura", cursive;
    font-weight: 400;
    font-size: 380px;
    color: var(--script-tan);
    line-height: 1;
  }
  .subtitle {
    position: absolute;
    left: 0; right: 0; top: 640px;
    margin: 0;
    text-align: center;
    font-family: "Raleway", sans-serif;
    font-weight: 300;
    font-size: 38px;
    line-height: 58px;
    color: var(--title-red);
  }
  .bottom-rule {
    position: absolute;
    left: 0; top: 1010px;
    width: 100%; height: 10px;
    background: var(--cover-red);
    box-shadow: 0 10px 0 0 var(--white);
  }
  .author-band {
    position: absolute;
    left: 0; top: 1030px;
    width: 100%; height: 170px;
    background: var(--cover-red);
    display: flex;
    align-items: center;
    justify-content: center;
  }
  .author-name {
    margin: 0;
    font-family: "Oswald", sans-serif;
    font-weight: 300;
    font-size: 92px;
    letter-spacing: 1px;
    text-transform: uppercase;
    color: var(--white);
    line-height: 1;
  }
</style>
</head>
<body>
  <main class="cover">
    <div class="top-band"></div>
    <div class="top-rule"></div>

    <h1 class="series-title">MAPLE-HOP</h1>
    <p class="script-title">Tots</p>

    <p class="subtitle">The natural way for your child<br>to be their best</p>

    <div class="bottom-rule"></div>
    <footer class="author-band">
      <p class="author-name">Dr. Hanne Solvik</p>
    </footer>
  </main>
</body>
</html>
```